2 Page Business Flyer for Finance Business

Need a two page flyer created for a finance business. Lots of text and needs to fit on two pages.

Corporate business/banking look and feel. Not too many large images. Lots of white space, clean design. Attached is color palette and the text contents of the flyer.

```html
<!DOCTYPE html>
<html lang="en">
<head>
<meta charset="utf-8">
<title>Vanilla Options Flyer</title>
<link href="https://fonts.googleapis.com/css2?family=Roboto:wght@300;400;500;700;900&display=swap" rel="stylesheet">
<style>
:root{
  --green:#72e4a8;
  --green-light:#93f0bd;
  --blue:#4a4cf0;
  --blue-title:#3b3ee0;
  --red:#c8222a;
  --slate:#3e4a4f;
  --text:#3a3a3a;
  --grey:#858f8c;
  --white:#ffffff;
}
*{margin:0;padding:0;box-sizing:border-box}
html,body{width:1200px;height:809px;overflow:hidden;background:var(--white)}
body{font-family:'Roboto',Arial,sans-serif;color:var(--text);position:relative}
.abs{position:absolute}
p{font-size:10px;line-height:12.6px;font-weight:300}

/* left page */
.intro-block{left:15px;top:12px;width:254px;height:424px;background:var(--green);color:var(--white);padding:8px 10px}
.intro-block .kicker{font-size:17px;font-weight:400}
.intro-block h1{font-size:42px;line-height:47px;font-weight:700;margin-top:4px;letter-spacing:.3px}
.intro-block p{color:var(--white);text-align:justify;margin-top:10px;font-weight:400}
.intro-block h1+p{margin-top:18px}
.photo{background:linear-gradient(135deg,#d9dfe3,#9aa6b0 55%,#5d6c7c)}
.photo-team{left:269px;top:12px;width:300px;height:299px}
.steps{left:276px;top:326px;width:290px;list-style:none}
.steps li{position:relative;padding-left:18px;font-size:10px;line-height:12.6px;font-weight:300;margin-bottom:13px}
.steps li::before{content:"";position:absolute;left:0;top:2px;width:8px;height:8px;border-radius:50%;background:#111}
.example-block{left:15px;top:475px;width:265px;height:116px;background:var(--blue);color:var(--white);padding:5px 8px}
.example-block .kicker{font-size:19px;font-weight:400}
.example-block h2{font-weight:400;font-size:38px;line-height:40px}
.example-block h2 strong{font-weight:700}
.example-body{left:17px;top:603px;width:263px}
.example-body p,.outcome-col p{text-align:justify;margin-bottom:12px}
.outcome-col{left:290px;top:475px;width:262px}
.grey-panel{left:290px;top:724px;width:262px;height:56px;background:var(--grey)}

/* right page */
.feature{top:13px;height:201px;background:var(--green-light);padding:10px 9px}
.feature h3{font-size:17px;font-weight:700;margin-bottom:6px}
.feature p{margin-bottom:10px}
.characteristics{left:626px;width:183px}
.advantages{left:814px;width:189px}
.risks{left:1008px;width:172px}
.characteristics h3,.advantages h3{color:var(--blue-title)}
.risks h3{color:var(--red)}
.section-kicker{font-size:18px;font-weight:400;color:var(--slate)}
.section-title{font-size:42px;font-weight:700;color:var(--slate);line-height:44px;letter-spacing:.5px}
.why{left:636px;top:236px;width:540px}
.why p{margin-top:10px;font-size:9.6px;line-height:12.4px}
.price{left:642px;top:384px;width:540px}
.price p{margin-top:8px;font-size:9.6px;line-height:12.4px}
.factors{left:642px;top:500px;width:288px;list-style:none}
.factors li{position:relative;padding-left:26px;font-size:9.8px;line-height:12.6px;font-weight:300;margin-bottom:11px;min-height:20px}
.factors li svg{position:absolute;left:0;top:-1px}
.photo-target{left:932px;top:502px;width:246px;height:298px;background:linear-gradient(160deg,#e9ecef,#bfc5c9 45%,#8b6b3e 80%,#d8c25a)}
.style-note{left:626px;top:700px;width:306px;height:100px;background:var(--blue);color:var(--white);padding:7px 14px}
.style-note p{color:var(--white);font-weight:400;font-size:9.8px;line-height:12.6px}
</style>
</head>
<body>

<section class="abs intro-block">
  <div class="kicker">How does a</div>
  <h1>VANILLA OPTION CONTRACT WORK?</h1>
  <p>The buyer of a vanilla option receives protection against an adverse movement in the exchange rate while allowing full participation in a beneficial move. At no time is the buyer of a Vanilla Option obligated to exercise the Option and transact the currencies, therefore providing flexibility in cases where the requirement to purchase foreign currency is not certain.</p>
  <p>A buyer of vanilla options is required to pay a premium (like an insurance premium) for the right, but not the obligation, to exchange currency at a predetermined rate on a predetermined date.</p>
</section>

<div class="abs photo photo-team" role="img" aria-label="Photo of three colleagues reviewing a document together in an office"></div>

<ul class="abs steps">
  <li>Set a protection rate which will be your worst-case scenario at expiry</li>
  <li>Determine the amount of currency you wish to protect</li>
  <li>Chose an expiry date for the contract</li>
  <li>Calculate the premium you are required to pay</li>
</ul>

<section class="abs example-block">
  <div class="kicker">Let’s look at an example:</div>
  <h2>YOU ARE IN<br><strong>IMPORTER.</strong></h2>
</section>

<div class="abs example-body">
  <p>Your construction company has bid on a project that if successful, will require you to import materials from the United States to use in construction. You have used todays pricing of materials in calculating your bid and want to protect against an adverse move in the US dollar exchange rate from eroding your margin if your bid is chosen for the project.</p>
  <p>You choose to buy a Vanilla Call which will protect you from a rise in the USD/CAD exchange rate above your protection rate. You choose to buy protection on $500,000 USD, with a protection rate (strike rate) of 1.3300 expiring 3 months from now. You are required to pay a premium which in this case is calculated to be 1.8%, or 11,970 CAD.</p>
</div>

<div class="abs outcome-col">
  <p>Your bid is successful: If the exchange rate is below your protection rate at expiration, you have no obligation relating to the vanilla call and you are free to buy USD at the cheaper spot rate. If the exchange rate is above your protection rate, your have the right to purchase your USD at the protection rate, and thereby claiming your insurance policy.</p>
  <p>Your bid is not successful: You have no obligation relating to the vanilla option however, if at expiry the exchange rate is above the protection rate, you may exercise your right to buy USD at the lower rate and simultaneous sell USD back at the prevailing spot rate, thereby recouping some or all of the premium paid to buy the option. Alternatively, if you find out your bid was not successful with time still left until expiration, you may sell your option back into the market in the case that it still has residual value, which will depend on various market factors.</p>
</div>
<div class="abs grey-panel"></div>

<section class="abs feature characteristics">
  <h3>Characteristics</h3>
  <p>You are looking for a straight-forward hedging solution</p>
  <p>You want to receive full benefit from an appreciation of the currency you are exposed to</p>
  <p>You are comfortable receiving protection at the strike rate of the option</p>
  <p>You are willing to pay the non-refundable premium</p>
</section>
<section class="abs feature advantages">
  <h3>Advantages</h3>
  <p>You hedge your foreign currency exposure at a predefined hedge rate</p>
  <p>You can choose the hedge rate that suits your budget requirements</p>
  <p>Provides the ability to fully participate in a favourable exchange rate move</p>
  <p>You can choose from most major currency pairs to meet your needs</p>
</section>
<section class="abs feature risks">
  <h3>Risks</h3>
  <p>Premium paid is non-refundable and remains your only obligation when buying vanilla options</p>
</section>

<section class="abs why">
  <div class="section-kicker">Why use</div>
  <h2 class="section-title">VANILLA OPTIONS?</h2>
  <p>Vanilla options are often compared to an insurance product. The buyer pays a non-refundable premium for the right, but not the obligation to trade currency in the future at the protection rate of the option. This product allows you to participate in a beneficial move to an unlimited extent, which will be the most advantageous outcome, if the exchange rate moves in your favour enough to more than offset the premium paid for the option.</p>
</section>

<section class="abs price">
  <div class="section-kicker">What determines the price of a</div>
  <h2 class="section-title">VANILLA OPTIONS?</h2>
  <p>The cost of an option is defined by the premium that is required to be paid in order to enter into the contract. Premiums are calculated using the industry standard formulas based upon the Black Scholes model. The most important variables in the option pricing formulas include the following:</p>
</section>

<ul class="abs factors">
  <li><svg width="18" height="18" viewBox="0 0 18 18"><circle cx="9" cy="9" r="7.5" fill="none" stroke="#4a4cf0" stroke-width="1.4"/><path d="M5 9l3 3 8-9" fill="none" stroke="#4a4cf0" stroke-width="2"/></svg>The current market Spot Rate.</li>
  <li><svg width="18" height="18" viewBox="0 0 18 18"><circle cx="9" cy="9" r="7.5" fill="none" stroke="#4a4cf0" stroke-width="1.4"/><path d="M5 9l3 3 8-9" fill="none" stroke="#4a4cf0" stroke-width="2"/></svg>Market volatility – the higher the volatility, the higher the premium.</li>
  <li><svg width="18" height="18" viewBox="0 0 18 18"><circle cx="9" cy="9" r="7.5" fill="none" stroke="#4a4cf0" stroke-width="1.4"/><path d="M5 9l3 3 8-9" fill="none" stroke="#4a4cf0" stroke-width="2"/></svg>The Term of the Option – a longer term typically results in a higher premium.</li>
  <li><svg width="18" height="18" viewBox="0 0 18 18"><circle cx="9" cy="9" r="7.5" fill="none" stroke="#4a4cf0" stroke-width="1.4"/><path d="M5 9l3 3 8-9" fill="none" stroke="#4a4cf0" stroke-width="2"/></svg>The Strike Rate – the closer to being ITM the protection rate is, the higher the premium.</li>
  <li><svg width="18" height="18" viewBox="0 0 18 18"><circle cx="9" cy="9" r="7.5" fill="none" stroke="#4a4cf0" stroke-width="1.4"/><path d="M5 9l3 3 8-9" fill="none" stroke="#4a4cf0" stroke-width="2"/></svg>The interest rate differential of the two currencies involved.</li>
  <li><svg width="18" height="18" viewBox="0 0 18 18"><circle cx="9" cy="9" r="7.5" fill="none" stroke="#4a4cf0" stroke-width="1.4"/><path d="M5 9l3 3 8-9" fill="none" stroke="#4a4cf0" stroke-width="2"/></svg>Style – European or American, or whether the option can be exercised prior to expiration</li>
</ul>

<div class="abs photo-target" role="img" aria-label="Photo of a hand placing a red dart in the centre of a yellow and black target"></div>

<section class="abs style-note">
  <p>An option can either a European (meaning that they can only be exercised on the expiry date), or American (meaning that they can be exercised at any time prior to expiration). We normally deals in European options however, we do offer American options under certain circumstances and when specific delivery terms are agreed upon between us and the customer.</p>
</section>

</body>
</html>
```